Business Book - Building Calm Habits at the Office (Less Noise, More Focus Each Day)

I'm looking for a cover that appeals to successful business people who are used to reading business titles.

The cover should feel familiar and fit in with the existing canon of bestselling business books with a vibrant, but professional look (see attached).

I want my book to stand out, but not to be frivolous. Abstract is probably best. Or close to it.

Please feel free to use my brand colours, or go with something else -

Teal
HEX #199BAB
25 / 155 / 171

Coral
HEX #EE786E
238 / 120/ 110

I don't want to include anything connected with robots or gendered assistants/business people. Or headsets.

It's only 24 hours which is mental

```html
<!DOCTYPE html>
<html lang="en">
<head>
<meta charset="UTF-8">
<title>Building Calm Habits at the Office — Cover</title>
<link rel="stylesheet" href="https://fonts.googleapis.com/css2?family=Kumbh+Sans:wght@400;600;700&display=swap">
<style>
  :root {
    --page: #ffffff;
    --teal: #199bab;
    --teal-deep: #147f8e;
    --teal-light: #2aa9b8;
    --coral: #ee786e;
    --coral-edge: #f6b3ab;
    --ink: #111111;
    --title: #ffffff;
  }
  * { margin: 0; padding: 0; box-sizing: border-box; }
  html, body {
    width: 1200px;
    height: 856px;
    overflow: hidden;
    background: var(--page);
  }
  .canvas {
    position: relative;
    width: 1200px;
    height: 856px;
    background: var(--page);
  }
  .cover {
    position: absolute;
    left: 313px;
    top: 46px;
    width: 574px;
    height: 764px;
    background: var(--teal);
    box-shadow: 0 2px 6px rgba(0,0,0,0.18);
    overflow: hidden;
    font-family: "Kumbh Sans", sans-serif;
  }
  .cover-art {
    position: absolute;
    inset: 0 0 14px 0;
    background:
      radial-gradient(ellipse at 70% 30%, rgba(255,255,255,0.10), transparent 60%),
      radial-gradient(ellipse at 25% 75%, rgba(0,0,0,0.12), transparent 55%),
      linear-gradient(160deg, var(--teal-light) 0%, var(--teal) 45%, var(--teal-deep) 100%);
  }
  .cover-band {
    position: absolute;
    left: 0;
    right: 0;
    bottom: 0;
    height: 14px;
    background: var(--coral);
  }
  .title {
    position: absolute;
    top: 52px;
    left: 0;
    right: 0;
    text-align: center;
    color: var(--title);
    font-weight: 600;
    text-transform: uppercase;
    line-height: 1;
    text-shadow: 0 2px 4px rgba(0,0,0,0.25);
  }
  .title-line { display: block; }
  .title-line--xl { font-size: 70px; letter-spacing: 1px; margin-bottom: 16px; }
  .title-line--md { font-size: 46px; letter-spacing: 1px; margin-bottom: 20px; }
  .title-line--rule {
    display: block;
    width: 400px;
    height: 2px;
    margin: 0 auto 16px;
    background: linear-gradient(90deg, transparent, var(--coral) 15%, var(--coral) 85%, transparent);
  }
  .subtitle {
    position: absolute;
    left: 57px;
    top: 519px;
    width: 460px;
    height: 122px;
    background: var(--coral);
    border: 2px solid var(--coral-edge);
    border-radius: 6px;
    box-shadow: 0 3px 6px rgba(0,0,0,0.25);
    display: flex;
    align-items: center;
    justify-content: center;
    text-align: center;
    color: var(--ink);
    font-size: 38px;
    font-weight: 400;
    line-height: 1.2;
  }
</style>
</head>
<body>
  <main class="canvas">
    <section class="cover">
      <div class="cover-art" role="img" aria-label="Faint abstract background of chat messages and document icons on a screen, in teal tones"></div>
      <h1 class="title">
        <span class="title-line title-line--xl">Building</span>
        <span class="title-line title-line--xl">Calm Habits</span>
        <span class="title-line title-line--md">at the</span>
        <span class="title-line title-line--xl" style="margin-bottom:4px">Office</span>
        <span class="title-line--rule"></span>
      </h1>
      <p class="subtitle">Less Noise, More Focus<br>Each Day</p>
      <div class="cover-band"></div>
    </section>
  </main>
</body>
</html>
```